Brivosta Films
Creative and Dynamic Independent Films
Professional
Marcus Tollen
OWNER/PRODUCER/
47 Haldon Ave
Quillmoor Heights QH 40512
Marcus@BrivostaFilms.com
www.BrivostaFilms.com
Bold,Regal,Elegant
Logo File.

```html
<!DOCTYPE html>
<html lang="en">
<head>
<meta charset="utf-8">
<title>Brivosta Films Stationery</title>
<link rel="stylesheet" href="https://fonts.googleapis.com/css2?family=Cinzel:wght@700&family=Open+Sans:wght@400;600&display=swap">
<style>
:root{
  --board:#c99a5e;
  --paper:#ffffff;
  --ink:#333a40;
  --muted:#7d8488;
  --brand:#2f3b45;
  --accent:#3f9fb5;
  --rule:#9aa2a6;
  --faint:rgba(47,59,69,.07);
}
*{box-sizing:border-box;margin:0;padding:0}
html,body{width:1200px;height:562px;overflow:hidden}
body{background:var(--board);font-family:"Open Sans",Arial,sans-serif;color:var(--ink);position:relative}
.sheet{position:absolute;background:var(--paper);box-shadow:0 2px 6px rgba(0,0,0,.35)}
.label{position:absolute;font-size:8px;font-weight:600;color:#3a2a18;text-align:center;width:100%;top:-14px;white-space:nowrap}
.mark{display:flex;align-items:center;gap:5px;font-family:"Cinzel",serif;font-weight:700;color:var(--brand);position:absolute;white-space:nowrap}
.mark .dot{width:14px;height:14px;border-radius:50%;background:var(--accent);flex:none}
.contact{position:absolute;font-size:5.5px;line-height:1.45;color:var(--ink);white-space:nowrap}
.ghost{position:absolute;left:50%;transform:translateX(-50%);font-family:"Cinzel",serif;font-weight:700;color:var(--faint);white-space:nowrap}
.fax-title{position:absolute;right:22px;top:120px;font-weight:600;font-size:10px}
.fax-table{position:absolute;left:22px;top:134px;width:309px;table-layout:fixed;border-collapse:collapse;font-size:6px}
.fax-table td{border:1px solid var(--rule);height:16px;padding:0 4px}
.fax-table td.key{width:42px;color:var(--muted)}
.checks{position:absolute;left:22px;width:309px;top:212px;display:flex;justify-content:space-between;font-size:6px;white-space:nowrap}
.checks span::before{content:"";display:inline-block;width:7px;height:7px;border:1px solid var(--ink);margin-right:3px;vertical-align:-1px}
.card-name{font-weight:600}
.flap{position:absolute;left:0;top:0}
</style>
</head>
<body>

<section class="sheet fax" style="left:36px;top:19px;width:353px;height:528px">
  <div class="label">Fax Cover</div>
  <div class="mark" style="left:22px;top:24px;font-size:13px"><span class="dot"></span>Brivosta Films</div>
  <div class="contact" style="left:200px;top:22px">Marcus Tollen<br>47 Haldon Ave<br>Quillmoor Heights QH 40512<br>Marcus@BrivostaFilms.com<br>www.BrivostaFilms.com</div>
  <div class="fax-title">FAX</div>
  <table class="fax-table">
    <tr><td class="key">To:</td><td></td><td class="key">From:</td><td></td></tr>
    <tr><td class="key">Fax:</td><td></td><td class="key">Pages:</td><td></td></tr>
    <tr><td class="key">Phone:</td><td></td><td class="key">Date:</td><td></td></tr>
    <tr><td class="key">Re:</td><td></td><td class="key">CC:</td><td></td></tr>
  </table>
  <div class="checks"><span>Urgent</span><span>For Review</span><span>Please Comment</span><span>Please Reply</span><span>Please Recycle</span></div>
  <div class="ghost" style="top:400px;font-size:40px">BRIVOSTA</div>
</section>

<section class="sheet letterhead" style="left:408px;top:34px;width:355px;height:513px">
  <div class="label">Letterhead</div>
  <div class="mark" style="left:22px;top:22px;font-size:13px"><span class="dot"></span>Brivosta Films</div>
  <div class="contact" style="left:200px;top:20px">Marcus Tollen<br>Tel: (555) 201-0148<br>47 Haldon Ave<br>Quillmoor Heights QH 40512<br>www.BrivostaFilms.com</div>
  <div class="ghost" style="top:250px;font-size:42px">BRIVOSTA</div>
</section>

<section class="sheet card-front" style="left:782px;top:29px;width:188px;height:120px;border-radius:6px">
  <div class="label">Business Card (Front)</div>
  <div class="mark" style="left:12px;top:18px;font-size:10px"><span class="dot"></span>Brivosta</div>
  <div class="contact" style="left:104px;top:30px"><span class="card-name">Marcus Tollen</span><br>Owner/Producer<br>47 Haldon Ave<br>Quillmoor Heights QH 40512<br>Marcus@BrivostaFilms.com</div>
</section>

<section class="sheet card-back" style="left:979px;top:29px;width:192px;height:120px;border-radius:6px">
  <div class="label">Business Card (Back)</div>
  <div class="mark" style="left:50%;top:40px;transform:translateX(-50%);font-size:13px"><span class="dot"></span>Brivosta</div>
  <div class="contact" style="left:0;right:0;top:70px;text-align:center">www.BrivostaFilms.com</div>
</section>

<section class="sheet envelope-front" style="left:782px;top:163px;width:389px;height:197px">
  <div class="label">Envelope (Front)</div>
  <div class="mark" style="left:16px;top:16px;font-size:12px"><span class="dot"></span>Brivosta Films</div>
  <div class="contact" style="left:30px;top:48px">47 Haldon Ave<br>Quillmoor Heights QH 40512</div>
</section>

<section class="sheet envelope-back" style="left:782px;top:379px;width:389px;height:163px">
  <div class="label">Envelope (Back)</div>
  <svg class="flap" width="389" height="163" viewBox="0 0 389 163" aria-hidden="true">
    <path d="M0 0 L194 92 L389 0" fill="none" stroke="#d7dbdd" stroke-width="1.5"/>
    <path d="M0 163 L160 80 M389 163 L229 80" fill="none" stroke="#e4e7e8" stroke-width="1"/>
  </svg>
  <div class="mark" style="left:50%;top:38px;transform:translateX(-50%);font-size:12px"><span class="dot"></span>Brivosta</div>
  <div class="contact" style="left:0;right:0;top:64px;text-align:center">47 Haldon Ave, Quillmoor Heights QH 40512</div>
</section>

</body>
</html>
```